Werbe Flyer an Hausbesitzer
Zielgruppe
Wir sind ein Immobilien Makler in Zürich. Wir werden den Werbe-Flyer zusammen mit einem Begleitschreiben und einem Rückantwort-Briefumschlag an Hausbesitzer per Post senden.
Zielgruppe:
ältere Leute, die Ihr Haus oder Wohnung verkaufen möchten.
Ziel:
Wir möchten den Maklerauftrag bekommen
Aufgabenstellung
Ein Werbe-Flyer erstellen.
Format:
A5
4 Seiten (Also A4 quer einmal gefaltet)
Hochformat
ein Beispiel liegt bei.
Der Text ist bereits definitiv.
Bilder und Layout ist frei wählbar.
Letzte Seite sollte abgetrennt werden können für die Rücksendung
Unsere Webpage als Info evtl. für Layout:
www.velaro-haus.ch

```html
<!DOCTYPE html>
<html lang="de">
<head>
<meta charset="utf-8">
<title>Velaro Haus AG – Rückantwort</title>
<link rel="stylesheet" href="https://fonts.googleapis.com/css2?family=Roboto+Condensed:wght@400;700&family=Arimo:wght@400;700&display=swap">
<style>
  :root {
    --navy: #05476a;
    --cyan: #3ec5d8;
    --white: #ffffff;
    --grey: #7a7a7a;
    --line: #c9d6de;
  }
  html, body { margin: 0; padding: 0; overflow: hidden; background: var(--white); }
  .flyer {
    position: relative; width: 1200px; height: 844px; overflow: hidden;
    background: var(--white);
    font-family: "Roboto Condensed", "Arial Narrow", sans-serif;
  }
  .brand {
    position: absolute; display: flex; align-items: center; gap: 10px;
    color: var(--navy); font-family: "Roboto Condensed", sans-serif; font-weight: 400;
    letter-spacing: 1.5px; text-transform: uppercase; white-space: nowrap;
  }
  .brand__mark { display: block; background: var(--cyan); }
  .brand--reply { left: 75px; top: 44px; font-size: 24px; }
  .brand--reply .brand__mark { width: 26px; height: 26px; }
  .brand--cover { left: 640px; top: 78px; font-size: 34px; }
  .brand--cover .brand__mark { width: 40px; height: 40px; }

  .reply {
    position: absolute; left: 0; top: 101px; width: 610px; height: 743px;
    background: var(--navy); color: var(--white);
  }
  .reply__title { position: absolute; left: 69px; top: 32px; margin: 0; font-size: 20px; font-weight: 400; }
  .reply__intro { position: absolute; left: 69px; top: 88px; margin: 0; font-size: 20px; line-height: 30px; }
  .options { position: absolute; left: 69px; top: 168px; margin: 0; padding: 0; list-style: none; font-size: 20px; }
  .options li { display: flex; align-items: center; gap: 9px; height: 40px; }
  .options .box { width: 12px; height: 12px; border: 2.5px solid var(--white); border-radius: 50%; }

  .fields { position: absolute; left: 69px; top: 331px; width: 446px; }
  .field { height: 63px; border-top: 1.5px solid var(--line); box-sizing: border-box; }
  .field span { display: block; margin-top: 5px; font-family: "Roboto Condensed", sans-serif; font-size: 18px; color: var(--cyan); }

  .footer {
    position: absolute; top: 814px; margin: 0; font-family: "Arimo", sans-serif;
    font-size: 10.5px; letter-spacing: 0.1px; white-space: nowrap; text-transform: uppercase;
  }
  .footer--reply { left: 25px; color: var(--white); font-weight: 700; }
  .footer--cover { left: 628px; color: var(--grey); }

  .cut-line { position: absolute; left: 606px; top: 50px; height: 770px; border-left: 2px dashed var(--cyan); }
  .scissors { position: absolute; left: 607px; top: 816px; }

  .gallery {
    position: absolute; left: 639px; top: 181px; width: 557px; height: 546px;
    box-sizing: border-box; padding: 5px; background: var(--cyan);
    display: grid; grid-template-columns: 1fr 1fr; grid-template-rows: 1fr 1fr; gap: 7px;
  }
  .photo { display: block; }
  .photo--modern {
    background:
      radial-gradient(ellipse 70% 45% at 55% 58%, rgba(236,232,226,0.95) 0%, rgba(214,200,182,0.7) 45%, rgba(214,200,182,0) 75%),
      linear-gradient(180deg, #2f6fc2 0%, #6f9fd6 35%, #c9d3dc 60%, #a89a86 82%, #6b8a3c 100%);
  }
  .photo--redroof {
    background:
      radial-gradient(ellipse 60% 22% at 55% 38%, rgba(196,82,44,0.85) 0%, rgba(196,82,44,0) 80%),
      radial-gradient(ellipse 70% 35% at 55% 65%, rgba(240,232,220,0.95) 0%, rgba(240,232,220,0) 80%),
      linear-gradient(180deg, #3f78c4 0%, #93b4dc 40%, #dcd6cc 68%, #6f9a3f 82%, #4f7a2c 100%);
  }
  .photo--tiled {
    background:
      radial-gradient(ellipse 75% 30% at 65% 28%, rgba(184,88,58,0.95) 0%, rgba(184,88,58,0) 85%),
      radial-gradient(ellipse 70% 35% at 50% 68%, rgba(222,202,170,0.95) 0%, rgba(222,202,170,0) 85%),
      linear-gradient(180deg, #d7dde2 0%, #c7a48e 40%, #d5c0a0 68%, #7d9a4a 85%, #5c7d38 100%);
  }
  .photo--green {
    background:
      radial-gradient(ellipse 55% 45% at 55% 55%, rgba(140,160,80,0.95) 0%, rgba(140,160,80,0) 85%),
      linear-gradient(180deg, #7fb0e0 0%, #b9d2e8 25%, #93ab5c 50%, #7f9c4a 72%, #3f6226 100%);
  }

  .web { position: absolute; right: 4px; top: 736px; margin: 0; font-family: "Arimo", sans-serif; font-size: 22px; color: var(--grey); }
</style>
</head>
<body>
<main class="flyer">
  <div class="brand brand--reply"><span class="brand__mark"></span>Velaro Haus AG</div>

  <section class="reply">
    <h2 class="reply__title">Ihre Rückantwort</h2>
    <p class="reply__intro">Bitte kreuzen Sie Ihre Wünsche an.<br>Ja, wir möchten …</p>
    <ul class="options">
      <li><span class="box"></span>… unsere Immobilie verkaufen</li>
      <li><span class="box"></span>… eine Immobilie kaufen</li>
      <li><span class="box"></span>… ein persönliches Gespräch</li>
    </ul>
    <div class="fields">
      <div class="field"><span>Name/Vorname</span></div>
      <div class="field"><span>Strasse</span></div>
      <div class="field"><span>PLZ/Ort</span></div>
      <div class="field"><span>Telefon</span></div>
      <div class="field"><span>E-Mail</span></div>
    </div>
  </section>

  <p class="footer footer--reply">Velaro Haus AG | Lindenweg 12 | 8008 Zürich | info@velaro-haus.ch | www.velaro-haus.ch</p>

  <div class="cut-line"></div>
  <svg class="scissors" width="14" height="14" viewBox="0 0 14 14" aria-hidden="true">
    <path d="M2 2 L12 12 M12 2 L2 12" stroke="#222" stroke-width="1.6" fill="none"/>
  </svg>

  <div class="brand brand--cover"><span class="brand__mark"></span>Velaro Haus AG</div>

  <div class="gallery">
    <div class="photo photo--modern" role="img" aria-label="Foto: modernes Einfamilienhaus mit Holzfassade und Balkon unter blauem Himmel"></div>
    <div class="photo photo--redroof" role="img" aria-label="Foto: weisses Haus mit rotem Ziegeldach und Rasen"></div>
    <div class="photo photo--tiled" role="img" aria-label="Foto: Klinkerhaus mit rotem Ziegeldach und Erker"></div>
    <div class="photo photo--green" role="img" aria-label="Foto: grünes Holzhaus mit Giebel und Garten"></div>
  </div>

  <p class="web">www.velaro-haus.ch</p>

  <p class="footer footer--cover">Velaro Haus AG | Lindenweg 12 | 8008 Zürich | info@velaro-haus.ch | www.velaro-haus.ch</p>
</main>
</body>
</html>
```